Marlin Freightways needs Bussiness cards!

Our new trucking company needs business cards!
We need the same design with two different names and emails, everything else it's the same.
I have included our original logo so we can use it for the design.
Note: the logo to be used is the o e with the buffalo on the right side, next to the letters B and E.

Target Market(s)

Trucking, refrigerated transportation, freight

Industry/Entity Type

Business

Contact Information for Business Card

Card #1:
Tomas Ruvalo
tomasruvalo@marlinfreightways.net
1-844-555-0193
(956)555-0172
3817 W. Alder Ave.
Pharr, TX 78590
www.marlinfreightways.net

Card#2:
Mirabel Quintana
mirabel@marlinfreightways.net
1-844-555-0193
(956)555-0172
3817 W. Alder Ave.
Pharr, TX 78590
www.marlinfreightways.net

Font styles to use
Sans Serif

Colors
0655a3
ec1f27
ffffff

Requirements
Must have
• our logo
Nice to have
• roads on background,

```html
<!DOCTYPE html>
<html lang="en">
<head>
<meta charset="utf-8">
<title>Marlin Freightways – Business Card</title>
<link rel="stylesheet" href="https://fonts.googleapis.com/css2?family=Roboto:wght@400;700;900&family=Roboto+Condensed:wght@400&display=swap">
<style>
  :root {
    --brand-blue: #0655a3;
    --deep-blue: #083a7a;
    --navy: #0a2f63;
    --brand-red: #ec1f27;
    --white: #ffffff;
    --page: #e9ebef;
  }
  * { box-sizing: border-box; margin: 0; padding: 0; }
  html, body { width: 1200px; height: 1023px; overflow: hidden; }
  body {
    background: var(--page);
    font-family: "Roboto", Arial, sans-serif;
    position: relative;
  }
  .card {
    position: absolute;
    left: 250px;
    width: 700px;
    height: 400px;
    border-radius: 18px;
    overflow: hidden;
    box-shadow: 0 8px 24px rgba(0,0,0,0.18);
  }
  .card-front { top: 70px; background: var(--white); }
  .card-back {
    top: 553px;
    background: radial-gradient(ellipse at 60% 45%, #1d63b8 0%, var(--brand-blue) 45%, var(--deep-blue) 100%);
    display: flex; align-items: center; justify-content: center;
  }

  .front-logo {
    position: absolute; left: 0; top: 0; width: 260px; height: 100%;
    display: flex; align-items: center; justify-content: center; gap: 10px;
  }
  .logo-mark {
    width: 20px; height: 20px; border-radius: 50%; background: var(--brand-red); flex: none;
  }
  .logo-name {
    font-weight: 900; font-size: 30px; line-height: 1.0; color: var(--brand-blue);
    letter-spacing: -0.5px;
  }

  .info-band {
    position: absolute; left: 260px; top: 0; right: 0; bottom: 0;
    background: linear-gradient(90deg, #3e79ad 0%, var(--brand-blue) 35%, var(--navy) 100%);
    border-left: 2px solid var(--brand-red);
  }
  .info-band::after {
    content: ""; position: absolute; left: 0; right: 0; bottom: 10px;
    height: 2px; background: var(--brand-red);
  }
  .person {
    position: absolute; left: 28px; top: 0; width: 150px; height: 100%;
    display: flex; flex-direction: column; justify-content: center;
  }
  .person-name { color: var(--brand-red); font-size: 20px; font-weight: 400; margin-bottom: 14px; white-space: nowrap; }
  .person-address {
    font-family: "Roboto Condensed", Arial, sans-serif;
    color: var(--white); font-size: 14px; line-height: 1.45; padding-left: 16px;
  }
  .divider {
    position: absolute; left: 190px; top: 100px; bottom: 100px;
    border-left: 1px dashed var(--brand-red);
  }
  .contacts {
    position: absolute; left: 206px; top: 0; right: 12px; height: 100%;
    display: flex; flex-direction: column; justify-content: center; gap: 9px;
    list-style: none;
  }
  .contacts li {
    display: flex; align-items: center; gap: 8px;
    font-family: "Roboto Condensed", Arial, sans-serif;
    color: var(--white); font-size: 13px; white-space: nowrap;
  }
  .contacts svg { width: 14px; height: 14px; flex: none; }

  .back-logo { display: flex; align-items: center; gap: 14px; }
  .back-logo .logo-name { color: var(--white); font-size: 54px; }
  .back-logo .logo-mark { width: 30px; height: 30px; }
</style>
</head>
<body>
  <section class="card card-front" aria-label="Business card front">
    <div class="front-logo">
      <span class="logo-mark"></span>
      <span class="logo-name">Marlin<br>Freightways</span>
    </div>
    <div class="info-band">
      <div class="person">
        <p class="person-name">Tomas Ruvalo</p>
        <p class="person-address">3817 W. Alder Ave.<br>Pharr, TX 78590</p>
      </div>
      <div class="divider"></div>
      <ul class="contacts">
        <li>
          <svg viewBox="0 0 16 16"><circle cx="8" cy="8" r="7" fill="none" stroke="#ec1f27" stroke-width="1.5"/><path d="M5.5 4.5l1.5 0 .6 2-1 .8a5 5 0 0 0 2.2 2.2l.8-1 2 .6v1.5c-3.5.5-6.6-2.6-6.1-6.1z" fill="#ec1f27"/></svg>
          (956)555-0172
        </li>
        <li>
          <svg viewBox="0 0 16 16"><rect x="2" y="6" width="12" height="8" rx="1.5" fill="#ec1f27"/><path d="M3 6c0-3 10-3 10 0" fill="none" stroke="#ec1f27" stroke-width="2"/></svg>
          1-844-555-0193
        </li>
        <li>
          <svg viewBox="0 0 16 16"><rect x="1.5" y="3.5" width="13" height="9" rx="1" fill="#ec1f27"/><path d="M2 4l6 5 6-5" fill="none" stroke="#ffffff" stroke-width="1.2"/></svg>
          tomasruvalo@marlinfreightways.net
        </li>
        <li>
          <svg viewBox="0 0 16 16" fill="none" stroke="#ec1f27" stroke-width="1.3"><circle cx="8" cy="8" r="6.5"/><ellipse cx="8" cy="8" rx="3" ry="6.5"/><path d="M1.5 8h13M3 4.5h10M3 11.5h10"/></svg>
          www.marlinfreightways.net
        </li>
      </ul>
    </div>
  </section>

  <section class="card card-back" aria-label="Business card back">
    <div class="back-logo">
      <span class="logo-mark"></span>
      <span class="logo-name">Marlin Freightways</span>
    </div>
  </section>
</body>
</html>
```